Radiology Department of an Hospital needs PowerPoint Design

The radiology Department performs X-Ray, Computed Tomography and Magnetic Resonance. We need a PowerPoint Design that includes the logo of the Hospital (file included) and our main business messages.

Target Market(s)

Business Presentations

Industry/Entity Type

Medicine

Requirements
Must have
• The logo of the Hospital (check uploaded file)

The name of the department - this is the main message:
"Serviço de Imagiologia - Alvedra, Lirena"

The slogan of the Department - it should go immediately bellow the name of the department in a smaller font size:
"Porque Cuidamos de Perto"

The main business messages or keywords of the Department:
"Rigor"
"Segurança"
"Proximidade"
Nice to have
• The logo in all pages.
The name of the Department in all pages, with the slogan.
The keywords well visible in the first page and maybe as large watermarks on following pages.

```html
<!DOCTYPE html>
<html lang="pt">
<head>
<meta charset="utf-8">
<title>VitaLumen Hospital – Serviço de Imagiologia – Presentation Slides</title>
<link rel="stylesheet" href="https://fonts.googleapis.com/css2?family=Open+Sans:wght@400;600;700;800&display=swap">
<style>
  :root{
    --teal:#0b5868;
    --teal-dark:#084452;
    --teal-deep:#073a47;
    --orange:#f5a800;
    --white:#ffffff;
    --paper:#f4f7f9;
    --ink:#1d2b33;
    --muted:#4a5a63;
    --photo-light:#dfe8ee;
    --photo-mid:#b9ccd8;
    --board:#000000;
  }
  *{box-sizing:border-box;margin:0;padding:0}
  html,body{width:1200px;height:699px;overflow:hidden;background:var(--board)}
  body{font-family:"Open Sans",Arial,sans-serif;color:var(--ink);position:relative}
  .slide{position:absolute;width:384px;height:216px;overflow:hidden;background:var(--white)}
  .c1{left:16px}.c2{left:408px}.c3{left:800px}
  .r1{top:12px}.r2{top:238px}.r3{top:464px}
  .abs{position:absolute}
  .photo{position:absolute;background:linear-gradient(135deg,var(--photo-light),var(--photo-mid))}
  .photo.cool{background:linear-gradient(135deg,#e8eef3,#9fb9c9)}
  .photo.dark{background:linear-gradient(135deg,#2d5f72,#7fa4b7)}

  .brand{position:absolute;display:flex;align-items:center;gap:5px}
  .brand-dot{border-radius:50%;background:var(--teal-dark);flex:none}
  .brand-name{font-weight:600;line-height:1;color:var(--teal-dark)}
  .brand.light .brand-dot{background:var(--white)}
  .brand.light .brand-name{color:var(--white)}
  .brand.sm .brand-dot{width:11px;height:11px}
  .brand.sm .brand-name{font-size:7.5px}
  .brand.lg .brand-dot{width:24px;height:24px}
  .brand.lg .brand-name{font-size:16px}

  .copy{font-size:4.3px;line-height:1.45;color:var(--muted)}
  .copy p+p{margin-top:4px}
  .copy.light{color:#d9e6ea}
  .title{font-weight:800;text-transform:uppercase;color:var(--teal-dark);letter-spacing:.2px}
  .title em{font-style:normal;color:var(--orange)}
  .title.light{color:var(--white)}

  .cover-band{position:absolute;left:0;right:0;top:160px;height:56px;background:linear-gradient(90deg,rgba(8,68,82,.95),rgba(11,88,104,.85))}
  .cover-head{font-size:12px;font-weight:700;color:var(--white);letter-spacing:.3px;white-space:nowrap}
  .cover-slogan{font-size:10px;color:var(--white);letter-spacing:.4px;margin-top:3px;white-space:nowrap}

  .dept-band{position:absolute;left:0;top:106px;width:203px;height:40px;background:linear-gradient(90deg,var(--teal-dark),var(--teal));padding:7px 0 0 18px}
  .dept-band h2{font-size:10px;line-height:1.25;font-weight:700;color:var(--white)}
  .slogan{font-size:9.5px;color:var(--teal-dark);letter-spacing:.3px;white-space:nowrap}
  .keywords{display:flex;gap:5px;align-items:center;font-size:7.5px;font-weight:700;color:var(--teal-dark)}
  .keywords i{width:3px;height:3px;border-radius:50%;background:var(--teal-dark)}

  .footer-bar{position:absolute;left:0;right:0;bottom:0;height:11px;background:var(--orange);display:flex;justify-content:space-between;align-items:center;padding:0 10px;font-size:4.5px;color:var(--ink)}
  .caption-title{font-size:4.8px;font-weight:700;color:var(--ink);margin-bottom:2px}

  .steps{position:absolute;left:200px;width:176px}
  .step{display:flex;gap:6px;margin-bottom:8px;align-items:flex-start}
  .step-num{flex:none;width:17px;height:17px;border-radius:50%;background:var(--orange);color:var(--white);font-size:6px;font-weight:700;display:flex;align-items:center;justify-content:center}
  .step h4{font-size:5px;font-weight:700;color:var(--orange);margin-bottom:1px}

  .socials{display:flex;gap:3px;align-items:center}
  .socials i{width:7px;height:7px;border-radius:50%;background:var(--orange)}
</style>
</head>
<body>

<section class="slide c1 r1">
  <div class="photo cool" role="img" aria-label="Patient lying on an MRI scanner table with a radiographer beside the machine" style="inset:0"></div>
  <div class="brand lg" style="left:12px;top:118px">
    <span class="brand-dot"></span><span class="brand-name">VitaLumen<br>Hospital</span>
  </div>
  <div class="cover-band"></div>
  <div class="abs" style="left:12px;top:170px">
    <div class="cover-head">SERVIÇO DE IMAGIOLOGIA - ALVEDRA, LIRENA</div>
    <div class="cover-slogan">PORQUE CUIDAMOS DE PERTO</div>
  </div>
</section>

<section class="slide c2 r1" style="background:var(--paper)">
  <div class="photo" role="img" aria-label="Radiologist in scrubs and mask holding up an X-ray film" style="left:180px;top:0;width:204px;height:216px"></div>
  <div class="brand lg" style="left:18px;top:62px">
    <span class="brand-dot"></span><span class="brand-name">VitaLumen<br>Hospital</span>
  </div>
  <div class="dept-band"><h2>SERVIÇO DE IMAGIOLOGIA<br>ALVEDRA, LIRENA</h2></div>
  <div class="abs slogan" style="left:18px;top:158px">PORQUE CUIDAMOS DE PERTO</div>
  <div class="abs keywords" style="left:18px;top:180px">RIGOR <i></i> SEGURANÇA <i></i> PROXIMIDADE</div>
</section>

<section class="slide c3 r1">
  <div class="abs title" style="left:10px;top:9px;font-size:10px">About our <em>Hospital</em></div>
  <div class="brand sm" style="left:308px;top:8px"><span class="brand-dot"></span><span class="brand-name">VitaLumen<br>Hospital</span></div>
  <div class="abs copy" style="left:10px;top:30px;width:150px">
    <p>Our imaging team delivers accurate diagnostic exams with modern equipment, careful protocols and a calm, patient first approach every day.</p>
    <p>X-ray, CT and MRI studies are reviewed by experienced radiologists so that every report reaches your doctor quickly and clearly.</p>
    <p>We keep radiation doses low, explain each step before the exam begins and stay close to patients from arrival to results.</p>
  </div>
  <div class="photo" role="img" aria-label="Doctor with stethoscope in a white coat" style="left:188px;top:28px;width:186px;height:100px"></div>
  <div class="abs copy" style="left:188px;top:134px;width:186px">
    <p>X-ray, CT and MRI studies are reviewed by experienced radiologists so that every report reaches your doctor quickly and clearly.</p>
    <p>Our imaging team delivers accurate diagnostic exams with modern equipment, careful protocols and a calm, patient first approach every day.</p>
  </div>
  <div class="footer-bar"><span>Copyright text here</span><span>Page: 10</span></div>
</section>

<section class="slide c1 r2">
  <div class="abs" style="left:0;top:0;width:384px;height:64px;background:var(--teal)"></div>
  <div class="abs title light" style="left:22px;top:21px;font-size:10px">Our project <em>overview</em></div>
  <div class="brand sm light" style="left:290px;top:8px"><span class="brand-dot"></span><span class="brand-name">VitaLumen<br>Hospital</span></div>
  <div class="abs copy light" style="left:22px;top:38px;width:330px">Our imaging team delivers accurate diagnostic exams with modern equipment, careful protocols and a calm, patient first approach every day.</div>
  <div class="photo" role="img" aria-label="Doctor speaking with a patient beside a CT scanner" style="left:22px;top:68px;width:158px;height:68px"></div>
  <div class="photo" role="img" aria-label="Nurse with a clipboard next to a patient on a scanner bed" style="left:202px;top:68px;width:158px;height:68px"></div>
  <div class="abs" style="left:22px;top:143px;width:158px">
    <div class="caption-title">Your Awesome Title Text One</div>
    <div class="copy">X-ray, CT and MRI studies are reviewed by experienced radiologists so that every report reaches your doctor quickly and clearly.</div>
  </div>
  <div class="abs" style="left:202px;top:143px;width:158px">
    <div class="caption-title">Your Awesome Title Text Two</div>
    <div class="copy">We keep radiation doses low, explain each step before the exam begins and stay close to patients from arrival to results.</div>
  </div>
  <div class="abs" style="left:0;right:0;bottom:0;height:8px;background:var(--orange)"></div>
</section>

<section class="slide c2 r2">
  <div class="photo" role="img" aria-label="Doctor standing beside a patient entering a CT scanner" style="left:216px;top:0;width:168px;height:216px"></div>
  <div class="brand sm" style="left:290px;top:8px"><span class="brand-dot"></span><span class="brand-name">VitaLumen<br>Hospital</span></div>
  <div class="abs title" style="left:24px;top:32px;font-size:10px;line-height:1.2">About our <em>creative<br>company</em></div>
  <div class="abs copy" style="left:24px;top:62px;width:170px">X-ray, CT and MRI studies are reviewed by experienced radiologists so that every report reaches your doctor quickly and clearly.</div>
  <div class="abs" style="left:0;top:112px;width:250px;height:88px;background:var(--teal);padding:10px 12px 0 24px">
    <div style="font-size:5.4px;font-weight:700;color:var(--white);line-height:1.35;margin-bottom:5px">Lorem ipsum dolor sit amet consectetur adipiscing elit sed do eiusmod tempor incididunt ut labore et dolore magna aliqua</div>
    <div class="copy light">We keep radiation doses low, explain each step before the exam begins and stay close to patients from arrival to results. Our imaging team delivers accurate diagnostic exams with modern equipment, careful protocols and a calm, patient first approach every day.</div>
  </div>
</section>

<section class="slide c3 r2" style="background:var(--teal)">
  <div class="photo dark" role="img" aria-label="Radiology control room with monitors showing scan images and a patient in the scanner beyond the glass" style="left:0;top:0;width:186px;height:216px"></div>
  <div class="abs title light" style="left:0;top:16px;background:var(--teal);padding:5px 8px;font-size:9.5px">Image title here</div>
  <div class="brand sm light" style="left:304px;top:8px"><span class="brand-dot"></span><span class="brand-name">VitaLumen<br>Hospital</span></div>
  <div class="steps" style="top:62px">
    <div class="step"><span class="step-num">01</span><div><h4>Your Awesome Headline Text One</h4><div class="copy light">Short supporting text for this point of the imaging service overview.</div></div></div>
    <div class="step"><span class="step-num">02</span><div><h4>Your Awesome Headline Text Two</h4><div class="copy light">Short supporting text for this point of the imaging service overview.</div></div></div>
    <div class="step"><span class="step-num">03</span><div><h4>Your Awesome Headline Text Three</h4><div class="copy light">Short supporting text for this point of the imaging service overview.</div></div></div>
    <div class="step"><span class="step-num">04</span><div><h4>Your Awesome Headline Text Four</h4><div class="copy light">Short supporting text for this point of the imaging service overview.</div></div></div>
  </div>
</section>

<section class="slide c1 r3" style="background:linear-gradient(135deg,var(--teal),var(--teal-dark))">
  <div class="brand sm light" style="left:304px;top:8px"><span class="brand-dot"></span><span class="brand-name">VitaLumen<br>Hospital</span></div>
  <div class="abs" style="left:12px;top:96px">
    <div style="font-size:17px;font-weight:700;color:var(--orange);line-height:1.1">SECTION TITLE HERE</div>
    <div style="font-size:11px;color:var(--white)">Subtext here</div>
  </div>
</section>

<section class="slide c2 r3" style="background:var(--paper)">
  <div class="abs" style="left:0;top:0;width:384px;height:26px;background:var(--teal)"></div>
  <div class="abs title light" style="left:10px;top:8px;font-size:9.5px">About our creative company</div>
  <div class="brand sm light" style="left:290px;top:7px"><span class="brand-dot"></span><span class="brand-name">VitaLumen<br>Hospital</span></div>
  <div class="photo" role="img" aria-label="Radiologist in blue cap and mask holding up X-ray films" style="left:0;top:26px;width:210px;height:178px"></div>
  <div class="abs" style="left:226px;top:50px;width:150px">
    <div style="font-size:11px;font-weight:700;color:var(--teal-dark);margin-bottom:4px">Image Title Here</div>
    <div style="font-size:5.4px;line-height:1.45;color:var(--muted)">
      <p>Lorem ipsum dolor sit amet, consectetur adipiscing elit, sed do eiusmod tempor incididunt ut labore et dolore magna aliqua. Ut enim ad minim veniam, quis nostrud exercitation ullamco laboris nisi ut aliquip ex ea commodo consequat. Duis aute irure dolor in reprehenderit in voluptate velit esse cillum dolore eu fugiat nulla pariatur. Lorem ipsum dolor sit amet, consectetur adipiscing elit.</p>
      <p style="margin-top:5px">Sed do eiusmod tempor incididunt ut labore et dolore magna aliqua. Ut enim ad minim veniam, quis nostrud exercitation ullamco laboris nisi ut aliquip ex ea commodo consequat.</p>
    </div>
  </div>
  <div class="abs" style="left:0;right:0;bottom:0;height:12px;background:var(--teal)"></div>
</section>

<section class="slide c3 r3" style="background:linear-gradient(135deg,var(--teal),var(--teal-deep))">
  <div class="brand lg light" style="left:30px;top:74px"><span class="brand-dot"></span><span class="brand-name">VitaLumen<br>Hospital</span></div>
  <div class="abs" style="left:188px;top:70px;width:180px">
    <div style="font-size:22px;font-weight:800;color:var(--white);line-height:1;margin-bottom:5px">THANK YOU</div>
    <div class="copy light" style="font-size:4.8px">Lorem ipsum dolor sit amet, consectetur adipiscing elit, sed do eiusmod tempor incididunt ut labore et dolore magna aliqua. Ut enim ad minim veniam, quis nostrud exercitation ullamco laboris nisi ut aliquip ex ea commodo consequat. Duis aute irure dolor in reprehenderit in voluptate velit esse cillum dolore eu fugiat nulla pariatur.</div>
    <div style="display:flex;gap:5px;align-items:center;margin-top:6px;font-size:4.8px;font-weight:700;color:var(--white)">Get In Touch <span class="socials"><i></i><i></i><i></i><i></i></span></div>
  </div>
</section>

</body>
</html>
```